KWCA '13 Presentation Dinner

Harrowfield Junior Hoops Circle Inc., or KWCA for short is a local basketball league based in Brisbane Southside, Australia.
We're holding our annual award presentation night and would like to advertise to our 350+ members via posters around the basketball hall and local shopping centres. Majority of our members are in aged 21-30.
The presentation dinner is held at a local Chinese restaurant with lucky door prize, raffles, trivia, '13 highlight video and presentation of '13 awards.
Essential Details are:
Location: Goldwillow Restaurant, 4/682 Fenner Rd, Sunnybank
Date: Saturday November 23rd 2013
Time: 6:00PM
Dress Code: Formal
See KWCA staff for more details
Optional Detail:
Cost: $400 per table of 10
Discount: Register before 14th September to receive $50 off - $350 per table
The final design should indicate this will be a fun night aimed at young adults and should not be missed by KWCA members.

```html
<!DOCTYPE html>
<html lang="en">
<head>
<meta charset="utf-8">
<title>KWCA 2013 Presentation Evening</title>
<link rel="stylesheet" href="https://fonts.googleapis.com/css2?family=Graduate&family=Alfa+Slab+One&family=Open+Sans:wght@400;700&display=swap">
<style>
  :root {
    --night: #0b1220;
    --navy: #141c33;
    --ember: #c23a0c;
    --flame: #f07a1e;
    --glow: #ffb04a;
    --white: #ffffff;
    --league-blue: #2a8fd0;
    --deep-blue: #1b5f99;
    --stamp-dark: #3a1c0c;
    --stamp-orange: #f29a2e;
  }
  html, body {
    margin: 0;
    padding: 0;
    width: 848px;
    height: 1200px;
    overflow: hidden;
    background: var(--night);
  }
  .poster {
    position: relative;
    width: 848px;
    height: 1200px;
    overflow: hidden;
    font-family: "Open Sans", Arial, sans-serif;
    color: var(--white);
  }
  .backdrop {
    position: absolute;
    inset: 0;
    background:
      radial-gradient(ellipse 55% 30% at 42% 22%, rgba(40,120,60,0.35), transparent 70%),
      linear-gradient(180deg, var(--night) 0%, var(--navy) 30%, #3a1408 50%, var(--ember) 66%, var(--flame) 82%, var(--glow) 100%);
  }
  .league-mark {
    position: absolute;
    left: 608px;
    top: 18px;
    width: 204px;
    height: 204px;
    border-radius: 50%;
    background: var(--league-blue);
    display: flex;
    align-items: center;
    justify-content: center;
    font-family: "Open Sans", Arial, sans-serif;
    font-weight: 700;
    font-size: 50px;
    color: var(--white);
  }
  .title-art {
    position: absolute;
    left: 0;
    top: 270px;
    width: 848px;
    height: 510px;
  }
  .title-art .league-name {
    font-family: "Graduate", Georgia, serif;
    font-size: 246px;
    fill: var(--white);
    stroke: var(--deep-blue);
    stroke-width: 6px;
    paint-order: stroke;
  }
  .title-art .season-year {
    font-family: "Graduate", Georgia, serif;
    font-size: 206px;
    fill: var(--league-blue);
    stroke: var(--white);
    stroke-width: 10px;
    paint-order: stroke;
  }
  .title-art .event-word {
    font-family: "Alfa Slab One", Georgia, serif;
    fill: url(#silverFade);
  }
  .event-date {
    position: absolute;
    left: 50px;
    top: 778px;
    margin: 0;
    font-size: 52px;
    line-height: 56px;
    font-weight: 400;
    white-space: nowrap;
  }
  .event-time {
    position: absolute;
    left: 266px;
    top: 826px;
    margin: 0;
    font-size: 52px;
    line-height: 56px;
  }
  .venue {
    position: absolute;
    right: 46px;
    top: 852px;
    margin: 0;
    text-align: right;
    font-size: 32px;
    line-height: 48px;
    font-style: normal;
  }
  .highlights {
    position: absolute;
    left: 30px;
    top: 900px;
    margin: 0;
    padding: 0;
    list-style: none;
    font-size: 23px;
    line-height: 34px;
    font-weight: 700;
  }
  .pricing-card {
    position: absolute;
    left: -6px;
    top: 1058px;
    width: 380px;
    padding: 10px 16px 10px 26px;
    background: var(--white);
    color: #222;
    font-size: 18px;
    line-height: 24px;
    transform: rotate(-8deg);
    transform-origin: left top;
    box-shadow: 0 3px 8px rgba(0,0,0,0.35);
  }
  .pricing-card p { margin: 0; }
  .pricing-card .label { color: var(--deep-blue); font-weight: 700; }
  .fun-stamp {
    position: absolute;
    left: 428px;
    top: 962px;
    width: 128px;
    height: 128px;
    transform: rotate(-6deg);
  }
  .fun-stamp text {
    font-family: "Open Sans", Arial, sans-serif;
    font-weight: 700;
    fill: var(--stamp-dark);
  }
  .dress-code {
    position: absolute;
    left: 30px;
    top: 1154px;
    margin: 0;
    font-size: 22px;
  }
  .dress-code strong { font-weight: 700; }
  .staff-note {
    position: absolute;
    right: 20px;
    top: 1152px;
    margin: 0;
    font-size: 20px;
  }
</style>
</head>
<body>
<main class="poster">
  <div class="backdrop" role="img" aria-label="Photo of a basketball player leaping to dunk at a hoop against a dark sky with green smoke above roaring flames"></div>

  <div class="league-mark">KWCA</div>

  <svg class="title-art" viewBox="0 0 848 510" aria-label="KWCA 2013 Presentation Evening">
    <defs>
      <linearGradient id="silverFade" x1="0" y1="0" x2="0" y2="1">
        <stop offset="0" stop-color="#ffffff"/>
        <stop offset="1" stop-color="#c9c2bd" stop-opacity="0.85"/>
      </linearGradient>
    </defs>
    <text class="league-name" x="424" y="225" text-anchor="middle" textLength="750" lengthAdjust="spacingAndGlyphs">KWCA</text>
    <text class="season-year" x="525" y="394" text-anchor="middle" textLength="430" lengthAdjust="spacingAndGlyphs">2013</text>
    <text class="event-word" x="90" y="450" font-size="78" textLength="708" lengthAdjust="spacingAndGlyphs">PRESENTATION</text>
    <text class="event-word" x="426" y="498" font-size="60" textLength="372" lengthAdjust="spacingAndGlyphs">EVENING</text>
  </svg>

  <p class="event-date">Saturday November 23rd 2013</p>
  <p class="event-time">6PM</p>

  <address class="venue">Goldwillow Restaurant<br>4/682 Fenner Rd,<br>Sunnybank</address>

  <ul class="highlights">
    <li>Lucky door prize, raffles, trivia,</li>
    <li>All the video highlights of 2013</li>
    <li>Presentation of '13 awards.</li>
  </ul>

  <div class="pricing-card">
    <p><span class="label">Cost:</span> $400 per table of 10</p>
    <p><span class="label">Discount:</span> Register before 14th September to receive $50 off - $350 per table</p>
  </div>

  <svg class="fun-stamp" viewBox="0 0 144 144" aria-label="Don't miss the fab date, 100% fun">
    <defs>
      <path id="stampArc" d="M 26 98 A 53 53 0 1 1 118 98"/>
    </defs>
    <circle cx="72" cy="72" r="70" fill="var(--stamp-dark)"/>
    <circle cx="72" cy="72" r="64" fill="var(--stamp-orange)"/>
    <circle cx="72" cy="72" r="36" fill="none" stroke="var(--stamp-dark)" stroke-width="3"/>
    <text font-size="10.5" letter-spacing="0.8"><textPath href="#stampArc" startOffset="50%" text-anchor="middle">DON'T MISS THE FAB DATE</textPath></text>
    <text x="72" y="70" font-size="17" text-anchor="middle">100%</text>
    <text x="72" y="90" font-size="19" text-anchor="middle">FUN</text>
  </svg>

  <p class="dress-code"><strong>Dress Code:</strong> Formal</p>
  <p class="staff-note">See KWCA staff for more details</p>
</main>
</body>
</html>
```